Business Card

We need a business card for a fundraising/sales and marketing company called Kelvora Appeals services. The logo colours are Red Black and white. The final design should communicate professional, reliable yet fun and charity minded
Updates

Sorry for the delay. A decision will be made in the next 48 hours. we are stuck between two designs. Kind Regards, Molly Ravenscroft

Industry/Entity Type

Marketing

```html
<!DOCTYPE html>
<html lang="en">
<head>
<meta charset="utf-8">
<title>Kelvora Appeals services – Stationery</title>
<link rel="stylesheet" href="https://fonts.googleapis.com/css2?family=Lato:wght@400;700&family=Cinzel:wght@400;700&display=swap">
<style>
  :root {
    --stage: #242424;
    --brand-red: #ec2227;
    --ink: #3d3d3d;
    --ink-soft: #777777;
    --paper: #ffffff;
    --paper-cool: #f4f5f6;
    --card-black: #000000;
    --label-grey: #4a4a4a;
    --figure-tone: #d9d9d9;
  }
  * { box-sizing: border-box; margin: 0; padding: 0; }
  html, body { width: 1200px; height: 940px; overflow: hidden; }
  body {
    background: var(--stage);
    font-family: "Lato", Arial, sans-serif;
    position: relative;
  }
  .sheet { position: absolute; overflow: hidden; }
  .icon { width: 8px; height: 8px; fill: var(--brand-red); display: inline-block; vertical-align: middle; }

  /* Wordmark */
  .wordmark {
    font-family: "Lato", Arial, sans-serif;
    font-weight: 700;
    letter-spacing: 0.04em;
    white-space: nowrap;
  }

  /* Presentation folder */
  .folder { left: 44px; top: 42px; width: 388px; height: 549px; background: var(--brand-red); }
  .folder .wordmark {
    position: absolute; top: 288px; left: 0; width: 100%;
    text-align: center; color: var(--paper); font-size: 22px;
  }
  .folder .folder-web {
    position: absolute; bottom: 8px; left: 0; width: 100%;
    text-align: center; color: var(--paper); font-size: 8px; font-weight: 700;
  }

  /* Letterhead */
  .letterhead { left: 490px; top: 42px; width: 388px; height: 549px; background: var(--paper); color: var(--ink); }
  .letterhead .wordmark { position: absolute; left: 34px; top: 58px; font-size: 12px; color: var(--brand-red); }
  .letterhead .contact-list {
    position: absolute; left: 222px; top: 38px; list-style: none;
    font-family: "Cinzel", Georgia, serif; font-size: 6.5px; line-height: 8px; color: var(--ink);
  }
  .letterhead .contact-list .icon { width: 7px; height: 7px; margin-right: 3px; }
  .letter-meta { position: absolute; top: 168px; left: 102px; width: 243px; font-size: 5.5px; }
  .letter-meta .meta-label { color: var(--brand-red); font-weight: 700; display: block; }
  .letter-meta .meta-subject { position: absolute; left: 0; top: 0; }
  .letter-meta .meta-date { position: absolute; left: 180px; top: 0; }
  .letter-side { position: absolute; top: 232px; left: 18px; width: 72px; text-align: right; font-size: 4.6px; line-height: 6px; color: var(--ink-soft); }
  .letter-side dt { color: var(--brand-red); font-weight: 700; }
  .letter-side dd { margin-bottom: 7px; }
  .letter-body { position: absolute; top: 214px; left: 102px; width: 243px; font-size: 5px; line-height: 7.3px; color: var(--ink-soft); }
  .letter-body .salutation { font-size: 8px; color: var(--ink); margin-bottom: 4px; }
  .letter-body p { margin-bottom: 7px; }
  .letter-sign { position: absolute; top: 410px; left: 102px; font-size: 6.5px; color: var(--ink-soft); }
  .letter-sign strong { display: block; font-size: 7px; color: var(--ink-soft); }
  .letter-sign span { font-size: 5px; }
  .letterhead .footer-bar { position: absolute; left: 48px; bottom: 0; width: 292px; height: 10px; background: var(--brand-red); }

  /* Business cards */
  .card { width: 188px; height: 329px; text-align: center; }
  .card-dark { left: 932px; top: 117px; background: var(--card-black); }
  .card-light { left: 932px; top: 484px; background: var(--paper-cool); }
  .card .wordmark { position: absolute; top: 70px; left: 0; width: 100%; font-size: 11px; color: var(--brand-red); }
  .card .name-bar { position: absolute; top: 129px; left: 12px; display: flex; height: 19px; }
  .card .name-bar .person { background: var(--brand-red); color: var(--paper); font-weight: 700; font-size: 10px; line-height: 19px; padding: 0 4px; }
  .card .name-bar .role { background: var(--label-grey); color: #e8e8e8; font-size: 7.5px; line-height: 19px; padding: 0 4px; }
  .card .card-contacts { position: absolute; top: 200px; left: 0; width: 100%; list-style: none; font-size: 8px; line-height: 10px; }
  .card .card-contacts li { margin-bottom: 0; }
  .card .card-contacts .icon { display: block; margin: 0 auto; }
  .card-dark .card-contacts { color: #8c8c8c; }
  .card-light .card-contacts { color: var(--ink); }
  .card .footer-bar { position: absolute; left: 26px; bottom: 0; width: 135px; height: 7px; background: var(--brand-red); }

  /* Envelope */
  .envelope { left: 44px; top: 630px; width: 564px; height: 282px; background: var(--paper); }
  .envelope .wordmark { position: absolute; left: 24px; top: 40px; font-size: 15px; color: var(--brand-red); }
  .envelope .side-bar { position: absolute; left: 0; top: 208px; width: 4px; height: 44px; background: var(--brand-red); }
  .envelope .contact-list {
    position: absolute; left: 19px; top: 207px; list-style: none;
    font-family: "Cinzel", Georgia, serif; font-size: 11px; line-height: 13.5px; color: var(--ink);
  }
  .envelope .contact-list .icon { width: 11px; height: 11px; margin-right: 4px; }
  .envelope .figure-group {
    position: absolute; left: 310px; top: 159px; width: 254px; height: 111px;
    background: linear-gradient(90deg, var(--figure-tone) 0%, #f5c6c6 30%, var(--figure-tone) 55%, #e4e4e4 100%);
    opacity: 0.7;
  }
</style>
</head>
<body>

<svg width="0" height="0" style="position:absolute" aria-hidden="true">
  <symbol id="icon-phone" viewBox="0 0 16 16"><path d="M2 5c0-2 2-3 6-3s6 1 6 3v1h-3V4.5H5V6H2zM4 7h8l2 6H2z"/></symbol>
  <symbol id="icon-mail" viewBox="0 0 16 16"><path d="M1 3h14v10H1zM2 4.2v.6l6 4 6-4v-.6z"/></symbol>
  <symbol id="icon-web" viewBox="0 0 16 16"><path d="M1 2h14v9H1zM2.5 3.5v6h11v-6zM6 12h4v1.5h2V15H4v-1.5h2z"/></symbol>
</svg>

<section class="sheet folder" aria-label="Presentation folder">
  <div class="wordmark">KELVORA APPEALS</div>
  <div class="folder-web">www.kelvoraappeals.com</div>
</section>

<section class="sheet letterhead" aria-label="Letterhead">
  <div class="wordmark">KELVORA APPEALS</div>
  <ul class="contact-list">
    <li><svg class="icon"><use href="#icon-phone"/></svg>0491 555 317</li>
    <li><svg class="icon"><use href="#icon-mail"/></svg>declan@kelvoraappeals.com</li>
    <li><svg class="icon"><use href="#icon-web"/></svg>www.kelvoraappeals.com</li>
  </ul>
  <div class="letter-meta">
    <div class="meta-subject"><span class="meta-label">SUBJECT:</span>Quarterly appeal review</div>
    <div class="meta-date"><span class="meta-label">DATE:</span>8th of May 2014</div>
  </div>
  <dl class="letter-side">
    <dt>Funding news</dt>
    <dd>Quarterly update<br>Donor care notes</dd>
    <dt>Local events</dt>
    <dd>Community drive this spring</dd>
  </dl>
  <div class="letter-body">
    <div class="salutation">Dear person,</div>
    <p>Thank you for your continued support of our community appeals this year. Your generosity has helped us reach more families, fund new local projects and train volunteers across the region. We are proud of what we have achieved together and grateful for every contribution.</p>
    <p>In the coming months we will launch a new giving programme designed to make donating simple and transparent. Supporters will receive regular updates showing exactly where their funds are going and the difference they make on the ground.</p>
    <p>We would welcome the chance to meet and discuss how we can work together on your next campaign. Please get in touch at your convenience.</p>
    <p>Yours Sincerely,</p>
  </div>
  <div class="letter-sign"><strong>Greta Lindqvist</strong><span>Founder</span></div>
  <div class="footer-bar"></div>
</section>

<section class="sheet card card-dark" aria-label="Business card, dark">
  <div class="wordmark">KELVORA APPEALS</div>
  <div class="name-bar"><span class="person">Declan Hartwell</span><span class="role">Managing Director</span></div>
  <ul class="card-contacts">
    <li><svg class="icon"><use href="#icon-phone"/></svg>0491 555 317</li>
    <li><svg class="icon"><use href="#icon-mail"/></svg>declan@kelvoraappeals.com</li>
    <li><svg class="icon"><use href="#icon-web"/></svg>www.kelvoraappeals.com</li>
  </ul>
  <div class="footer-bar"></div>
</section>

<section class="sheet card card-light" aria-label="Business card, light">
  <div class="wordmark">KELVORA APPEALS</div>
  <div class="name-bar"><span class="person">Declan Hartwell</span><span class="role">Managing Director</span></div>
  <ul class="card-contacts">
    <li><svg class="icon"><use href="#icon-phone"/></svg>0491 555 317</li>
    <li><svg class="icon"><use href="#icon-mail"/></svg>declan@kelvoraappeals.com</li>
    <li><svg class="icon"><use href="#icon-web"/></svg>www.kelvoraappeals.com</li>
  </ul>
  <div class="footer-bar"></div>
</section>

<section class="sheet envelope" aria-label="Envelope">
  <div class="wordmark">KELVORA APPEALS</div>
  <div class="side-bar"></div>
  <ul class="contact-list">
    <li><svg class="icon"><use href="#icon-phone"/></svg>0491 555 317</li>
    <li><svg class="icon"><use href="#icon-mail"/></svg>declan@kelvoraappeals.com</li>
    <li><svg class="icon"><use href="#icon-web"/></svg>www.kelvoraappeals.com</li>
  </ul>
  <div class="figure-group" role="img" aria-label="Faint decorative group of standing figures in grey with one in light red"></div>
</section>

</body>
</html>
```